Aerial Imaging and photgraphy business card

Design a business card with eye catching aerial photo of country side / landscape with a drone in the foreground.
Also contact details.

Target Market(s)

Aerial Imaging photography

Industry/Entity Type

Advertising

Contact Information for Business Card

Corwin
0412905316
Website http://www.skylarkvistas.com.au/
email address : skylarkvistas.com.au

Colors
e8f1ca
cadf82
9bcb3c
33a6d7
85cae6
cee9f5

Requirements
Must have
• High res photo
• KPV drone in the foreground Either T4200 and kpv Hovera or both
Nice to have
• high resolution landscape country photo on the front of the card with a KPV T4200 drone in the foreground.

```html
<!DOCTYPE html>
<html lang="en">
<head>
<meta charset="utf-8">
<title>Skylark Vistas – Business Card</title>
<link rel="stylesheet" href="https://fonts.googleapis.com/css2?family=Arimo:wght@400;700&display=swap">
<style>
  :root {
    --pale-green: #e8f1ca;
    --light-green: #cadf82;
    --green: #9bcb3c;
    --deep-green: #7db52a;
    --blue: #33a6d7;
    --light-blue: #85cae6;
    --pale-blue: #cee9f5;
    --ink: #1d1d1d;
    --paper: #ffffff;
    --backdrop: #e9eaec;
  }
  * { box-sizing: border-box; margin: 0; padding: 0; }
  html, body { width: 1200px; height: 1200px; overflow: hidden; }
  body {
    background: var(--backdrop);
    font-family: "Arimo", Arial, sans-serif;
    position: relative;
  }
  .card {
    position: absolute;
    left: 150px;
    width: 900px;
    height: 510px;
    background: var(--paper);
    box-shadow: 0 6px 18px rgba(0,0,0,.12);
    overflow: hidden;
  }
  .card--back { top: 70px; display: flex; }
  .card--front { top: 620px; }

  .brand {
    width: 42%;
    display: flex;
    align-items: center;
    justify-content: center;
    gap: 14px;
  }
  .brand__mark {
    width: 30px; height: 30px; border-radius: 50%;
    background: var(--blue);
  }
  .brand__name {
    font-weight: 700;
    font-size: 34px;
    color: var(--ink);
    text-transform: uppercase;
    letter-spacing: 1px;
  }

  .bands { width: 58%; display: flex; flex-direction: column; }
  .band { display: flex; align-items: center; padding-left: 36px; color: var(--ink); }
  .band--pale { height: 12%; background: var(--pale-green); }
  .band--light { height: 12%; background: var(--light-green); }
  .band--name { height: 22%; background: var(--green); }
  .band--phone { height: 15%; background: var(--deep-green); }
  .band--web { height: 15%; background: var(--blue); }
  .band--mail { height: 14%; background: var(--light-blue); }
  .band--foot { height: 10%; background: var(--pale-blue); }

  .contact__name { font-size: 50px; font-weight: 400; text-transform: uppercase; letter-spacing: 1px; }
  .contact__line { font-size: 17px; text-transform: uppercase; display: flex; align-items: center; gap: 16px; }
  .icon { width: 38px; height: 38px; flex: none; }

  .strip { position: absolute; left: 0; width: 100%; display: flex; }
  .strip--top { top: 0; height: 16px; }
  .strip--bottom { bottom: 0; height: 60px; }
  .strip span { flex: 1; }
  .c1 { background: var(--pale-blue); }
  .c2 { background: var(--light-blue); }
  .c3 { background: var(--blue); }
  .c4 { background: var(--green); }
  .c5 { background: var(--light-green); }
  .c6 { background: var(--pale-green); }

  .photo {
    position: absolute;
    top: 16px; bottom: 60px; left: 0; right: 0;
    background: linear-gradient(180deg, #4f86c0 0%, #8db4d6 42%, #b9cfdc 52%, #2f6fa4 60%, #1f5684 78%, #9c6a36 100%);
  }
</style>
</head>
<body>
  <section class="card card--back">
    <div class="brand">
      <span class="brand__mark"></span>
      <span class="brand__name">Skylark Vistas</span>
    </div>
    <div class="bands">
      <div class="band band--pale"></div>
      <div class="band band--light"></div>
      <div class="band band--name"><span class="contact__name">Corwin</span></div>
      <div class="band band--phone">
        <span class="contact__line">
          <svg class="icon" viewBox="0 0 40 40"><circle cx="20" cy="20" r="17" fill="none" stroke="#1d1d1d" stroke-width="2.5"/><path d="M14 12c-2 2-2 5 1 9s7 7 10 7c2 0 3-1 3-2l-3-3-3 1c-2-1-4-3-5-5l1-3-3-3z" fill="#1d1d1d"/></svg>
          0412905316
        </span>
      </div>
      <div class="band band--web">
        <span class="contact__line">
          <svg class="icon" viewBox="0 0 40 40"><circle cx="20" cy="20" r="17" fill="none" stroke="#1d1d1d" stroke-width="2.5"/><circle cx="20" cy="20" r="9" fill="none" stroke="#1d1d1d" stroke-width="2"/><path d="M11 20h18M20 11c-4 5-4 13 0 18M20 11c4 5 4 13 0 18" fill="none" stroke="#1d1d1d" stroke-width="1.6"/></svg>
          www.skylarkvistas.com.au
        </span>
      </div>
      <div class="band band--mail">
        <span class="contact__line">
          <svg class="icon" viewBox="0 0 40 40"><circle cx="20" cy="20" r="17" fill="none" stroke="#1d1d1d" stroke-width="2.5"/><rect x="11" y="14" width="18" height="12" fill="none" stroke="#1d1d1d" stroke-width="2"/><path d="M11 14l9 7 9-7" fill="none" stroke="#1d1d1d" stroke-width="2"/></svg>
          info@skylarkvistas.com.au
        </span>
      </div>
      <div class="band band--foot"></div>
    </div>
  </section>

  <section class="card card--front">
    <div class="strip strip--top"><span class="c1"></span><span class="c2"></span><span class="c3"></span><span class="c4"></span><span class="c5"></span><span class="c6"></span></div>
    <div class="photo" role="img" aria-label="Photo of a KPV Hovera drone hovering in the foreground over a rocky coastline and blue sea under a clear sky"></div>
    <div class="strip strip--bottom"><span class="c1"></span><span class="c2"></span><span class="c3"></span><span class="c4"></span><span class="c5"></span><span class="c6"></span></div>
  </section>
</body>
</html>
```